Business Card Design Project

looking for business cards with new logo

I am looking to keep with the colors of the logo i posted.  Here are some other details to consider.  I would like my website prominently displayed on the business card with the logo.  my website is www.HavenrockTX.com...it should be spelled this way.

My contact information is:

Daniel P Whitcomb III
Broker/Owner
48391 Cordell Ave., Suite 307
Helotes, Texas 78023
Office: 210-555-0147
Email:  Daniel@HavenrockTX.com

Thank you
Daniel Whitcomb

```html
<!DOCTYPE html>
<html lang="en">
<head>
<meta charset="utf-8">
<title>Havenrock Realty Business Cards</title>
<link rel="stylesheet" href="https://fonts.googleapis.com/css2?family=Roboto:wght@400;500;700&family=Roboto+Condensed:wght@700&display=swap">
<style>
  :root {
    --backdrop: #2a2a2c;
    --navy: #163f6e;
    --sky: #3aa3de;
    --white: #ffffff;
    --ink: #3a3a3c;
    --soft-white: #e6edf5;
  }
  * { margin: 0; padding: 0; box-sizing: border-box; }
  html, body { width: 1200px; height: 900px; overflow: hidden; }
  body {
    background: var(--backdrop);
    font-family: "Roboto", Arial, sans-serif;
    position: relative;
  }
  .card {
    position: absolute;
    width: 520px;
    height: 300px;
    border-radius: 30px;
    overflow: hidden;
  }
  .card-back {
    left: 50px; top: 300px;
    background: var(--navy);
    color: var(--white);
    display: flex;
    flex-direction: column;
    align-items: center;
    justify-content: center;
  }
  .brand {
    display: flex;
    align-items: center;
    gap: 12px;
    font-weight: 500;
    font-size: 44px;
    letter-spacing: 0.5px;
  }
  .brand-mark {
    width: 16px; height: 16px;
    background: var(--sky);
  }
  .card-back .brand { color: var(--white); }
  .back-website {
    margin-top: 34px;
    font-family: "Roboto Condensed", Arial, sans-serif;
    font-weight: 700;
    font-size: 15px;
    letter-spacing: 0.6px;
  }
  .card-front {
    left: 630px; top: 300px;
    background: var(--white);
  }
  .front-shape { position: absolute; inset: 0; }
  .card-front .brand {
    position: absolute;
    left: 50px; top: 42px;
    font-size: 38px;
    color: var(--ink);
  }
  .holder {
    position: absolute;
    left: 44px; top: 176px;
    color: var(--white);
  }
  .holder-name {
    font-family: "Roboto Condensed", Arial, sans-serif;
    font-weight: 700;
    font-size: 17px;
    letter-spacing: 0.5px;
  }
  .holder-title { font-size: 11px; color: var(--soft-white); margin-top: 1px; }
  .office { margin-top: 22px; font-size: 12px; line-height: 1.3; }
  .office-company { color: var(--sky); }
  .contacts {
    position: absolute;
    left: 305px; top: 232px;
    list-style: none;
    color: var(--white);
    font-size: 12.5px;
  }
  .contacts li { display: flex; align-items: center; gap: 12px; height: 17px; }
  .contacts svg { width: 11px; height: 11px; flex: none; }
  .contacts strong { font-weight: 700; }
  .contacts .accent { color: var(--sky); font-weight: 700; }
</style>
</head>
<body>
  <section class="card card-back" aria-label="Card back">
    <div class="brand"><span class="brand-mark"></span>Havenrock Realty</div>
    <p class="back-website">www.HavenrockTX.com</p>
  </section>

  <section class="card card-front" aria-label="Card front">
    <svg class="front-shape" viewBox="0 0 520 300" preserveAspectRatio="none" aria-hidden="true">
      <path d="M0 122 C120 118 300 150 520 212 L520 300 L0 300 Z" fill="var(--navy)"/>
      <path d="M0 108 C130 104 300 132 470 198 C300 146 120 118 0 119 Z" fill="var(--sky)"/>
      <path d="M74 125 L112 125 L93 142 Z" fill="var(--white)" stroke="var(--sky)" stroke-width="2"/>
    </svg>

    <div class="brand"><span class="brand-mark"></span>Havenrock Realty</div>

    <div class="holder">
      <h1 class="holder-name">DANIEL P WHITCOMB III</h1>
      <p class="holder-title">Broker/Owner</p>
      <p class="office">
        <span class="office-company">HAVENROCK REALTY LLC</span><br>
        48391 Cordell Ave., Suite 307<br>
        Helotes, Texas 78023
      </p>
    </div>

    <ul class="contacts">
      <li><svg viewBox="0 0 12 12"><rect x="2" y="1" width="8" height="10" rx="1" fill="var(--sky)"/></svg>210-555-0147</li>
      <li><svg viewBox="0 0 12 12"><rect x="0.5" y="2.5" width="11" height="7" fill="var(--sky)"/><path d="M0.5 2.5 L6 7 L11.5 2.5" fill="none" stroke="var(--navy)" stroke-width="1"/></svg><span><strong>Daniel</strong>@HavenrockTX.com</span></li>
      <li><svg viewBox="0 0 12 12"><circle cx="6" cy="6" r="5.3" fill="var(--sky)"/></svg><span>www.<span class="accent">HavenrockTX</span>.com</span></li>
    </ul>
  </section>
</body>
</html>
```